Wedding Program

Miriam and Owen are getting married. They are looking for a simple 4-page program that conveys the special day. Venue is a museum in a large East-Coast city: classic 18th century, formal. Ceremony is non-religious. Party includes a photo booth and DJ.

He's a math geek - she's an activist/educator.

Please incorporate unique design sensibility - be creative! Colors of purple, eggplant, ivory, and gray are the couple's choice. Fall motif OK.

Target Market(s)

ages 25 - 85, members of a family

Industry/Entity Type

Graphic Design

Font styles to use
Serif
Decorative

Colors
8769ae
b7a5cd
fece3e
f78f20
757575
cfcfcf
6b449b
a64599
fffaee

Requirements
Must have
• Readable, attractive 4-color design using the copy and image provided in the attachment.
Nice to have
• It's a LOVE-ly day for a wedding - be creative!
Should not have
• Avoid flowery girly-girl fonts or obvious hearts and flowers stuff.

```html
<!DOCTYPE html>
<html lang="en">
<head>
<meta charset="utf-8">
<title>Wedding Program – The Wedding Party</title>
<link href="https://fonts.googleapis.com/css2?family=Cormorant+Garamond:wght@500;700&family=Dancing+Script:wght@600&display=swap" rel="stylesheet">
<style>
  :root {
    --paper: #fdf8ef;
    --lace: #f7d9b8;
    --lace-soft: rgba(247, 217, 184, 0);
    --accent: #f78f20;
    --ink: #3b3232;
  }
  * { margin: 0; padding: 0; box-sizing: border-box; }
  html, body { width: 1200px; height: 840px; overflow: hidden; background: var(--paper); }
  .spread {
    position: relative;
    width: 1200px;
    height: 840px;
    background: var(--paper);
    font-family: "Cormorant Garamond", Georgia, serif;
    color: var(--ink);
    overflow: hidden;
  }
  .lace {
    position: absolute;
    top: 0;
    height: 840px;
  }
  .lace--left  { left: 0; width: 190px; background: linear-gradient(90deg, var(--lace) 0%, var(--lace-soft) 100%); opacity: .55; }
  .lace--center { left: 470px; width: 320px; background: linear-gradient(90deg, var(--lace-soft) 0%, var(--lace) 50%, var(--lace-soft) 100%); opacity: .45; }
  .lace--right { right: 0; width: 210px; background: linear-gradient(270deg, var(--lace) 0%, var(--lace-soft) 100%); opacity: .55; }

  .party-title {
    position: absolute;
    left: 140px;
    top: 160px;
    font-family: "Dancing Script", cursive;
    font-weight: 600;
    font-size: 38px;
    color: var(--accent);
    letter-spacing: .5px;
  }
  .list {
    position: absolute;
    list-style: none;
    text-align: center;
    font-variant: small-caps;
    font-weight: 500;
    font-size: 16px;
    letter-spacing: .3px;
  }
  .list li { display: flex; align-items: center; justify-content: center; white-space: nowrap; }
  .list .role { font-weight: 700; margin-right: 5px; }

  .party-list { left: 0; width: 600px; top: 256px; }
  .party-list li { height: 53.8px; }

  .order-list { left: 600px; width: 600px; top: 120px; }
  .order-list li { height: 46px; }
</style>
</head>
<body>
<main class="spread">
  <div class="lace lace--left" role="img" aria-label="Pale peach lace ornament along the left edge"></div>
  <div class="lace lace--center" role="img" aria-label="Pale peach lace ornament at the centre fold"></div>
  <div class="lace lace--right" role="img" aria-label="Pale peach lace ornament along the right edge"></div>

  <section class="page page--party">
    <h1 class="party-title">The Wedding Party</h1>
    <ul class="list party-list">
      <li><span class="role">Bride and Groom:</span> Miriam (Mimi) Harlow and Owen Bellamy</li>
      <li><span class="role">Bride’s Parents:</span> Gerald and Louise Harlow</li>
      <li><span class="role">Groom’s Parents:</span> Walter and Diane Bellamy</li>
      <li><span class="role">Bridesmaids:</span> Nora Bellamy, Tessa Quill, Clara Dunmore</li>
      <li><span class="role">Groomsmen:</span> Eli Bellamy, Martin Harlow, Declan Moss, Arjun Velkar</li>
      <li><span class="role">Grandparent of the Bride:</span> Edith Kowalin</li>
      <li><span class="role">Grandparents of the Groom:</span> Harold Bellamy, Vernon Ashby</li>
      <li><span class="role">Celebrant:</span> Celeste Marrow</li>
    </ul>
  </section>

  <section class="page page--order">
    <ol class="list order-list">
      <li>Processional</li>
      <li>Greeting</li>
      <li>Blessing of the Rings</li>
      <li>Presentation of the Bride and Groom</li>
      <li>Reading: Henry Ellis Crane, The Orchard at Fallow Creek</li>
      <li>Promises and Wedding Vows</li>
      <li>Exchange of Wedding Rings</li>
      <li>Wine Box and Love Letters</li>
      <li>Signing of Marriage Certificate</li>
      <li>Declaration of Support</li>
      <li>Reading: Samuel Reed, The Long Way Home</li>
      <li>Declaration of Marriage and The Kiss</li>
      <li>Recessional</li>
    </ol>
  </section>
</main>
</body>
</html>
```